Gutschein für Onlineshop DIN A Lang
Zielgruppe
Wir betreiben unter www.feldkiste-online.example einen Onlineshop für Armee- und Outdoorbekleidung sowie Ausrüstung. Für eine Paketbeilage benötigen wir einen Gutschein
Aufgabenstellung
Erstellung eines Gutscheins im DIN A Lang Format (Kuvert) mit Vorder- und Rückseite im CI der Webseite. Logo kann gerne zur Verfügung gestellt werden.
Gutscheincode, Wert und Laufzeit wird noch mitgeteilt.

```html
<!DOCTYPE html>
<html lang="de">
<head>
<meta charset="utf-8">
<title>Gutschein Feldkiste – Vorder- und Rückseite</title>
<link rel="stylesheet" href="https://fonts.googleapis.com/css2?family=Stardos+Stencil:wght@400;700&family=Ubuntu:wght@500;700&family=Arimo:wght@400&display=swap">
<style>
  :root {
    --khaki: #a19c63;
    --khaki-light: #a5a86c;
    --olive-dark: #474a2b;
    --ink: #2c2b26;
    --text-dark: #2f2e22;
    --earth-dark: #2f251f;
    --earth-mid: #5a4536;
    --leather: #6d5546;
    --paper: #ffffff;
  }
  html, body { margin: 0; padding: 0; overflow: hidden; background: var(--paper); }
  .canvas {
    position: relative;
    width: 1191px;
    height: 1200px;
    overflow: hidden;
    background: var(--paper);
  }
  .side {
    position: absolute;
    left: 0;
    width: 1191px;
    height: 540px;
    overflow: hidden;
  }
  .side--front { top: 0; }
  .side--back { top: 660px; }

  .photo {
    position: absolute;
    inset: 0;
  }
  .photo--front {
    background: radial-gradient(ellipse at 30% 55%, var(--leather) 0%, var(--earth-mid) 35%, var(--earth-dark) 75%),
                var(--earth-dark);
  }
  .photo--back {
    background: radial-gradient(ellipse at 65% 50%, var(--leather) 0%, var(--earth-mid) 40%, var(--earth-dark) 80%),
                var(--earth-dark);
  }

  .torn-panel {
    position: absolute;
    top: 0;
    height: 540px;
  }
  .torn-panel--front { right: 0; width: 300px; }
  .torn-panel--back { left: 0; width: 290px; }

  /* Front */
  .title-band {
    position: absolute;
    left: 16px;
    top: 222px;
    width: 925px;
    height: 84px;
    background: var(--khaki-light);
    transform: rotate(-6.3deg);
    transform-origin: 0 0;
    display: flex;
    align-items: center;
    justify-content: center;
  }
  .title-band__word {
    font-family: "Stardos Stencil", serif;
    font-weight: 700;
    font-size: 96px;
    letter-spacing: 3px;
    color: var(--olive-dark);
    line-height: 1;
    margin-top: 6px;
  }
  .url-strip {
    position: absolute;
    left: 38px;
    top: 342px;
    width: 922px;
    height: 40px;
    background: var(--khaki-light);
    transform: rotate(-6.3deg);
    transform-origin: 0 0;
    display: flex;
    align-items: center;
    padding-left: 82px;
    box-sizing: border-box;
  }
  .url-strip__text {
    font-family: "Ubuntu", sans-serif;
    font-weight: 700;
    font-size: 15.5px;
    color: var(--text-dark);
    white-space: nowrap;
  }
  .value {
    position: absolute;
    left: 1080px;
    top: 170px;
    transform: translate(-50%, -50%) rotate(90deg);
    font-family: "Stardos Stencil", serif;
    font-weight: 700;
    font-size: 150px;
    line-height: 1;
    color: var(--ink);
    white-space: nowrap;
  }
  .brand-name {
    position: absolute;
    left: 965px;
    top: 398px;
    font-family: "Stardos Stencil", serif;
    font-weight: 700;
    font-size: 44px;
    line-height: 46px;
    color: var(--olive-dark);
  }

  /* Back */
  .contact {
    position: absolute;
    left: 12px;
    top: 358px;
    font-family: "Ubuntu", sans-serif;
    font-weight: 700;
    font-size: 12.5px;
    line-height: 17px;
    color: var(--text-dark);
  }
  .contact p { margin: 0; }
  .contact__address { margin-bottom: 26px !important; }

  .note-band {
    position: absolute;
    left: 267px;
    top: 378px;
    width: 556px;
    height: 132px;
    background: var(--khaki-light);
    transform: rotate(-2.5deg);
    transform-origin: 0 0;
    padding: 30px 24px 0 36px;
    box-sizing: border-box;
  }
  .note-band__text {
    margin: 0;
    font-family: "Arimo", sans-serif;
    font-size: 14px;
    line-height: 18px;
    color: var(--text-dark);
  }
</style>
</head>
<body>
<div class="canvas">

  <section class="side side--front" aria-label="Vorderseite">
    <div class="photo photo--front" role="img" aria-label="Foto: abgetragene braune Lederstiefel auf Rindenmulch"></div>

    <svg class="torn-panel torn-panel--front" viewBox="0 0 300 540" preserveAspectRatio="none" aria-hidden="true">
      <polygon fill="var(--khaki)" points="22,0 300,0 300,540 4,540 8,500 2,460 10,420 6,380 14,340 8,300 16,260 10,220 18,180 12,140 20,100 14,60 24,30"/>
    </svg>

    <div class="title-band"><span class="title-band__word">GUTSCHEIN</span></div>
    <div class="url-strip"><span class="url-strip__text">www.feldkiste-online.example - bei uns finden Sie die größte Auswahl an Bundeswehrbekleidung!</span></div>

    <div class="value">25€</div>
    <div class="brand-name">FELD<br>KISTE</div>
  </section>

  <section class="side side--back" aria-label="Rückseite">
    <div class="photo photo--back" role="img" aria-label="Foto: abgetragene Lederstiefel von vorn auf Rindenmulch"></div>

    <svg class="torn-panel torn-panel--back" viewBox="0 0 290 540" preserveAspectRatio="none" aria-hidden="true">
      <polygon fill="var(--khaki)" points="0,0 222,0 230,40 222,80 236,120 228,160 240,200 232,240 246,280 240,320 252,360 246,400 260,440 254,480 266,540 0,540"/>
    </svg>

    <div class="contact">
      <p class="contact__address">Nordlicht Versand GmbH<br>Division Feldkiste<br>Am Heidegraben 8<br>12345 Musterstadt<br>Germany</p>
      <p>Tel.: 01234/567890<br>Fax: 01234/567891<br>mail: kontakt@feldkiste-online.example</p>
    </div>

    <div class="note-band">
      <p class="note-band__text">Gutschein über 25€<br>Lorem ipsum dolor sit amet, consetetur sadipscing elitr, sed diam nonumy eirmod tempor invidunt ut labore et dolore magna aliquyam erat, sed diam voluptua. At vero eos et accusam et justo duo dolores et ea rebum. Stet clita kasd gubergren, no sea takimata sanctus est Lorem ipsum dolor sit amet.</p>
    </div>
  </section>

</div>
</body>
</html>
```